Website for PeakStride Functional Training

We would like to launch a website for our boutique gym, PeakStride Functional Training. We'd like the website to have a lot of lime green which is one of our colors in our logo. The website will have a description of our workouts, membership, free trial class and location information.

Target Market(s)

Fitness enthusiasts, health conscious people, target ages 20-65, people looking to get fit and healthy, people looking to lose weight

Industry/Entity Type

Gym

Coding

Number of Pages Required

1 page

Font styles to use
Serif

Colors
9ccb3b
34a7d8

Requirements
Must have
• A lot of lime green to match our logo. Let the website be fun, eye catchy. Our phone number which is 614-287-9153 to be easily dialed directly from our website.
Nice to have
• We would like to include this verbiage:
• -The Most FUN 1 hour workout
• -Affordable personal training/group training
• -Individualized workout programs
• -FUN workouts delivering results
• -Turn ON fat burn-The Most FUN 1 hour workout
• -Turn ON fat burning "EPOC" after burn
• We want our website to be easily seen on smart phones, iPads, Androids
Should not have
• Font that is hard on the eyes

```html
<!DOCTYPE html>
<html lang="en">
<head>
<meta charset="utf-8">
<title>PeakStride Functional Training</title>
<link rel="stylesheet" href="https://fonts.googleapis.com/css2?family=Montserrat:wght@400;500;600;700&family=Lato:wght@300;400;700;900&display=swap">
<style>
:root{
  --lime:#8ef200;
  --lime-deep:#7bd400;
  --blue:#3ec5ee;
  --ink:#1b1b1b;
  --dark:#262626;
  --grey-text:#5a5a5a;
  --card-foot:#ededed;
  --white:#ffffff;
  --heading:'Montserrat', sans-serif;
  --body:'Lato', sans-serif;
}
*{margin:0;padding:0;box-sizing:border-box}
html,body{width:1200px;height:3377px;overflow:hidden;background:var(--white)}
body{position:relative;font-family:var(--body);color:var(--ink)}
.abs{position:absolute}
.btn{position:absolute;display:flex;align-items:center;justify-content:center;border-radius:30px;font-family:var(--body);font-weight:700;text-transform:uppercase;letter-spacing:.5px;text-decoration:none}
.section-title{position:absolute;left:0;width:1200px;text-align:center;font-family:var(--heading);font-weight:500;font-size:48px;letter-spacing:1px;color:var(--ink)}
.section-sub{position:absolute;left:270px;width:660px;text-align:center;font-size:17px;line-height:28px;color:var(--grey-text)}

/* header */
.hero{left:0;top:0;width:1200px;height:675px;background:linear-gradient(100deg,#3a2a26 0%,#5b3a2c 35%,#a65a2c 62%,#e7823a 82%,#f39a4a 100%)}
.nav{left:0;top:0;width:1200px;height:63px;background:#151515}
.nav-link{position:absolute;top:21px;font-family:var(--heading);font-size:15px;font-weight:500;color:var(--white);letter-spacing:.5px}
.nav-link.active{color:var(--lime)}
.logo-tab{left:488px;top:0;width:224px;height:108px;background:#151515;border-radius:0 0 112px 112px / 0 0 50px 50px}
.logo-name{left:488px;top:22px;width:224px;text-align:center;font-family:var(--heading);font-weight:700;font-size:28px;color:var(--lime);line-height:32px}
.logo-sub{left:488px;top:58px;width:224px;text-align:center;font-family:var(--heading);font-weight:700;font-size:17px;color:var(--lime)}
.signup{left:1018px;top:12px;width:103px;height:40px;background:var(--lime);color:var(--ink);font-size:15px}
.hero-line{left:79px;font-family:var(--body);color:var(--white)}

/* workouts */
.workout{top:867px;width:261px;height:331px}
.workout-name{position:absolute;left:0;top:196px;width:100%;text-align:center;font-size:26px;color:var(--ink)}
.workout .btn{left:47px;top:250px;width:167px;height:49px;background:var(--white);color:var(--blue);font-size:18px}

/* featured */
.feature-title{left:601px;top:1255px;font-family:var(--heading);font-weight:500;font-size:48px;line-height:50px;letter-spacing:1px}
.feature-text{left:601px;top:1366px;width:520px;font-size:15.5px;line-height:23px;color:var(--grey-text)}
.thumb{top:1495px;height:105px}
.dark-btn{background:var(--dark);color:var(--white)}

/* trainers */
.trainer{top:1927px;width:252px;height:387px;background:var(--card-foot)}
.trainer-photo{position:absolute;left:0;top:0;width:252px;height:250px}
.trainer-name{position:absolute;top:270px;width:100%;text-align:center;font-family:var(--heading);font-weight:600;font-size:20px}
.trainer-role{position:absolute;top:302px;width:100%;text-align:center;font-size:13px;font-style:italic;letter-spacing:2px;color:#666}
.trainer-social{position:absolute;top:340px;left:0;width:100%;display:flex;justify-content:center;gap:22px}
.dot{width:14px;height:14px;border-radius:50%;background:#555}

/* trial & membership */
.trial-title{left:0;top:2360px;width:1200px;text-align:center;font-family:var(--heading);font-weight:500;font-size:48px;letter-spacing:1px}
.trial-text{left:258px;top:2424px;width:684px;text-align:center;font-size:17px;line-height:25px;color:var(--grey-text)}
.member-title{left:79px;top:2733px;font-family:var(--heading);font-weight:500;font-size:48px;letter-spacing:1px;color:var(--ink)}
.member-text{left:79px;top:2800px;width:520px;font-size:16px;line-height:23px;color:#3f6d00}

/* newsletter */
.field{left:315px;top:3084px;width:412px;height:52px;border:1px solid #cfcfcf;border-radius:26px;padding-left:34px;display:flex;align-items:center;font-size:14px;font-style:italic;color:#888}
.subscribe{left:743px;top:3084px;width:142px;height:52px;background:var(--lime);color:var(--ink);font-size:16px}

/* footer */
.footer{left:0;top:3190px;width:1200px;height:187px;background:#171717}
.foot-link{position:absolute;top:3220px;font-size:14px;font-weight:700;color:var(--white);letter-spacing:.5px}
.gallery{left:79px;top:3210px;width:104px;height:46px;background:var(--lime);color:var(--ink);font-size:14px}
.social{position:absolute;top:3211px;width:46px;height:46px;border-radius:50%;background:#4a4a4a}
.social.on{background:var(--lime)}
.foot-rule{left:79px;top:3278px;width:1042px;height:1px;background:#333}
.ico{position:absolute;top:3298px;width:44px;height:44px;background:var(--lime);display:flex;align-items:center;justify-content:center}
.foot-text{position:absolute;color:var(--white)}
</style>
</head>
<body>

<!-- Hero -->
<div class="abs hero" role="img" aria-label="Photo of a woman lifting kettlebells overhead in a warm-lit gym"></div>
<div class="abs nav"></div>
<a class="nav-link active" style="left:76px">HOME</a>
<a class="nav-link" style="left:149px">ABOUT</a>
<a class="nav-link" style="left:230px">CLASSES</a>
<a class="nav-link" style="left:323px">MEMBERSHIP</a>
<div class="abs logo-tab"></div>
<div class="abs logo-name">PEAKSTRIDE</div>
<div class="abs logo-sub">Functional Training</div>
<a class="nav-link" style="left:772px">BLOG</a>
<a class="nav-link" style="left:842px">CONTACT</a>
<a class="nav-link" style="left:942px">LOGIN</a>
<a class="btn signup">Sign-Up</a>

<div class="abs hero-line" style="top:198px;font-size:56px;font-weight:400;line-height:70px">Turn <span style="color:var(--lime);font-weight:900;font-size:76px">ON</span></div>
<div class="abs hero-line" style="top:290px;font-size:64px;line-height:76px"><b style="font-weight:900">FAT</b> Burn</div>
<div class="abs" style="left:79px;top:392px;width:130px;height:2px;background:var(--white)"></div>
<div class="abs hero-line" style="top:400px;font-size:32px;line-height:40px">The Most <b style="font-weight:900">FUN 1 Hour</b></div>
<div class="abs hero-line" style="top:442px;font-size:32px;line-height:40px;color:var(--blue);font-weight:700">Workout</div>
<a class="btn" style="left:79px;top:502px;width:184px;height:50px;background:var(--lime-deep);color:var(--white);font-size:17px;border:2px solid #c9ff7a">Explore</a>

<!-- Workouts -->
<h2 class="section-title" style="top:722px">OUR WORKOUTS</h2>
<p class="section-sub" style="top:782px">Lorem Ipsum is simply dummy text of the printing and typesetting industry. Lorem Ipsum has been the industry's</p>

<div class="abs workout" style="left:79px;background:linear-gradient(160deg,#b4f53a,#8ef200)" role="img" aria-label="Lime-tinted photo of a personal training session">
  <div class="workout-name">Personal Training</div><a class="btn">Book Now</a></div>
<div class="abs workout" style="left:340px;background:linear-gradient(160deg,#7ed7f3,#3ec5ee)" role="img" aria-label="Blue-tinted photo of people in a one hour workout">
  <div class="workout-name">1 Hour Workout</div><a class="btn">Book Now</a></div>
<div class="abs workout" style="left:601px;background:linear-gradient(160deg,#b4f53a,#8ef200)" role="img" aria-label="Lime-tinted photo of a fat burning class">
  <div class="workout-name">Fat Burning</div><a class="btn">Book Now</a></div>
<div class="abs workout" style="left:862px;width:259px;background:linear-gradient(160deg,#7ed7f3,#3ec5ee)" role="img" aria-label="Blue-tinted photo of a group training class">
  <div class="workout-name">Group Training</div><a class="btn">Book Now</a></div>

<!-- Featured classes -->
<svg class="abs" style="left:0;top:1227px" width="1200" height="513" viewBox="0 0 1200 513">
  <polygon points="0,400 600,240 1200,245 1200,513 0,513" fill="var(--lime)"/>
</svg>
<div class="abs" style="left:0;top:1230px;width:552px;height:500px;background:radial-gradient(ellipse at 50% 45%,#6d7480 0%,#3c3f44 45%,rgba(60,63,68,0) 72%)" role="img" aria-label="Photo of a man in athletic wear lunging forward"></div>
<h2 class="abs feature-title">TOP FEATURED<br>CLASSES</h2>
<p class="abs feature-text">Lorem Ipsum is simply dummy text of the printing and typesetting industry. Lorem Ipsum has been the industry's standard dummy text ever since the 1500s, when an unknown printer took a galley of type and scrambled it to make a type specimen book.</p>
<div class="abs thumb" style="left:601px;width:160px;background:linear-gradient(135deg,#4a5a4a,#7b8a6a)" role="img" aria-label="Video still of a workout class"></div>
<svg class="abs" style="left:658px;top:1524px" width="46" height="46" viewBox="0 0 46 46"><circle cx="23" cy="23" r="23" fill="var(--lime)"/><polygon points="18,13 33,23 18,33" fill="var(--ink)"/></svg>
<div class="abs thumb" style="left:774px;width:169px;background:linear-gradient(135deg,#9fc7e0,#8fb36a)" role="img" aria-label="Photo of an outdoor stretching class"></div>
<div class="abs thumb" style="left:954px;width:167px;background:linear-gradient(135deg,#6fae4a,#b7d68a)" role="img" aria-label="Photo of partners training on grass"></div>
<a class="btn dark-btn" style="left:601px;top:1636px;width:164px;height:50px;font-size:17px">View More</a>

<!-- Trainers -->
<h2 class="section-title" style="top:1786px">OUR TRAINERS</h2>
<p class="section-sub" style="top:1846px">Lorem Ipsum is simply dummy text of the printing and typesetting industry. Lorem Ipsum has been the industry's</p>

<div class="abs trainer" style="left:79px">
  <div class="trainer-photo" style="background:linear-gradient(180deg,#d4d6d2,#b9bcb7)" role="img" aria-label="Portrait of the founder in training gear"></div>
  <div class="trainer-name">Nadia Holloway</div><div class="trainer-role">FOUNDER &amp; OWNER</div>
  <div class="trainer-social"><span class="dot"></span><span class="dot"></span><span class="dot"></span><span class="dot"></span></div></div>
<div class="abs trainer" style="left:344px">
  <div class="trainer-photo" style="background:linear-gradient(180deg,#c9b598,#a88b68)" role="img" aria-label="Portrait of the aqua fitness trainer"></div>
  <div class="trainer-name">Marcus Reed</div><div class="trainer-role">AQUA FITNESS</div>
  <div class="trainer-social"><span class="dot"></span><span class="dot"></span><span class="dot"></span><span class="dot"></span></div></div>
<div class="abs trainer" style="left:608px">
  <div class="trainer-photo" style="background:linear-gradient(180deg,#f2f2f2,#dcdcdc)" role="img" aria-label="Portrait of the dance trainer flexing"></div>
  <div class="trainer-name">Lena Brooks</div><div class="trainer-role">DANCING</div>
  <div class="trainer-social"><span class="dot"></span><span class="dot"></span><span class="dot"></span><span class="dot"></span></div></div>
<div class="abs trainer" style="left:871px;width:250px">
  <div class="trainer-photo" style="width:250px;background:linear-gradient(180deg,#c6cbc6,#9ea49e)" role="img" aria-label="Portrait of the fitness trainer holding a dumbbell"></div>
  <div class="trainer-name">Owen Calder</div><div class="trainer-role">FITNESS</div>
  <div class="trainer-social"><span class="dot"></span><span class="dot"></span><span class="dot"></span><span class="dot"></span></div></div>

<!-- Free trial & membership -->
<div class="abs" style="left:0;top:2341px;width:565px;height:360px;background:linear-gradient(110deg,#e8d6c2 0%,#c9a88a 40%,#f3e7d8 80%,rgba(255,255,255,0) 100%)" role="img" aria-label="Photo of a woman stretching outdoors in sunlight"></div>
<h2 class="abs trial-title">FREE TRIAL FOR YOU</h2>
<p class="abs trial-text">Lorem Ipsum is simply dummy text of the printing and typesetting industry. Lorem Ipsum has been the industry's standard dummy text ever since the 1500s, when an unknown printer took a galley of type and scrambled it to make a type specimen book.</p>
<a class="btn" style="left:506px;top:2521px;width:185px;height:50px;background:var(--lime);color:var(--ink);font-size:17px">Join Us Now</a>

<svg class="abs" style="left:0;top:2690px" width="1200" height="218" viewBox="0 0 1200 218">
  <polygon points="0,10 660,0 1200,60 1200,218 0,218" fill="var(--lime)"/>
</svg>
<div class="abs" style="left:720px;top:2465px;width:450px;height:443px;background:radial-gradient(ellipse at 55% 45%,#f3a7a9 0%,#e9b59a 35%,rgba(233,181,154,0) 70%)" role="img" aria-label="Photo of a cheering woman with a megaphone"></div>
<h2 class="abs member-title">GET MEMBERSHIP</h2>
<p class="abs member-text">Lorem Ipsum is simply dummy text of the printing and typesetting industry. Lorem Ipsum has been the industry's standard dummy text ever since the 1500s, when an unknown printer took a galley of type.</p>
<a class="btn dark-btn" style="left:630px;top:2814px;width:185px;height:50px;font-size:17px">Regiter Now</a>

<!-- Newsletter -->
<h2 class="section-title" style="top:2953px">NOT SURE YET?</h2>
<p class="section-sub" style="top:3016px;font-size:16px;line-height:25px">Then Sign Up For Our Newsleeter &amp; Get all News &amp; Updates, Classes &amp; Workouts on Just One Click.</p>
<div class="abs field">E-mail</div>
<a class="btn subscribe">Subscribe</a>

<!-- Footer -->
<div class="abs footer"></div>
<a class="btn gallery">Gallery</a>
<a class="foot-link" style="left:213px">EQUIPMENT</a>
<a class="foot-link" style="left:351px">FAQS</a>
<span class="social on" style="left:961px"></span>
<span class="social" style="left:1018px"></span>
<span class="social" style="left:1075px"></span>
<div class="abs foot-rule"></div>

<div class="ico" style="left:79px"><svg width="22" height="26" viewBox="0 0 22 26"><path d="M11 1a9 9 0 0 0-9 9c0 7 9 15 9 15s9-8 9-15a9 9 0 0 0-9-9z" fill="none" stroke="#1b1b1b" stroke-width="2"/><circle cx="11" cy="10" r="3" fill="#1b1b1b"/></svg></div>
<div class="foot-text" style="left:138px;top:3299px;font-size:13.5px;line-height:21px">123 Building Name, Area,<br>City, Country - Zipcode</div>
<div class="ico" style="left:342px"><svg width="24" height="24" viewBox="0 0 24 24"><path d="M6 2l4 5-2 3c1.5 3 3.5 5 6 6l3-2 5 4-2 4C10 22 2 14 2 4z" fill="none" stroke="#1b1b1b" stroke-width="2" stroke-linejoin="round"/></svg></div>
<a class="foot-text" href="tel:6142879153" style="left:401px;top:3305px;font-size:24px;text-decoration:none">614-287-9153</a>
<div class="ico" style="left:603px"><svg width="24" height="18" viewBox="0 0 24 18"><rect x="1" y="1" width="22" height="16" fill="none" stroke="#1b1b1b" stroke-width="2"/><path d="M1 1l11 9 11-9" fill="none" stroke="#1b1b1b" stroke-width="2"/></svg></div>
<div class="foot-text" style="left:666px;top:3310px;font-size:16px">info@peakstride.com</div>
<span class="abs" style="left:873px;top:3297px;width:46px;height:46px;border-radius:50%;background:var(--lime)"></span>
<div class="foot-text" style="left:952px;top:3299px;font-size:14px;line-height:21px;font-weight:700">© <span style="color:var(--lime)">PEAKSTRIDE</span> - 2016. All<br>Rights Reserved.</div>

</body>
</html>
```